A webite for an Urgent Care for children

We need a design for a new website for an Urgent care for kids. We are based in Atlanta, GA and provide quality after-hours and urgent care services for children. We will appreciate an innovative design that employs flash technology, especially on the Home page. We also want there to be a Contact Us form. There should also be a control panel with the ability for us to make quick and minor edits on the website as needed without requiring the services of an expert.

Target Market(s)

Parents, children, general audience

Industry/Entity Type

Healthcare

Coding

Coded - Design and coding required

Number of Pages Required

5+ page

Font styles to use
Sans Serif
Decorative

Colors
acd037
acd136
cadf82
eaf2ce
f6faec

Requirements
Must have
• Mobile devices website capable
• Link to social media, Facebook, twitter, etc
Nice to have
• Ability for customers to pay online.

```html
<!DOCTYPE html>
<html lang="en">
<head>
<meta charset="utf-8">
<title>PLAYPATH Urgent Care</title>
<link rel="stylesheet" href="https://fonts.googleapis.com/css2?family=Patrick+Hand&family=Source+Sans+3:wght@400;600;700&display=swap">
<style>
:root{
  --lime:#acd037;
  --lime-text:#a6cb34;
  --lime-soft:#cadf82;
  --page-bg:#e8e8e8;
  --ink:#3a3a3a;
  --muted:#555;
  --footer:#1b1b1b;
  --white:#fff;
  --col-a:#f4f4f4;
  --col-b:#eeeeee;
  --col-c:#e6e6e6;
  --sky-top:#a9e0f7;
  --sky-low:#d7f1fb;
  --grass:#9fdc16;
  --grass-deep:#7cc51a;
}
*{box-sizing:border-box;margin:0;padding:0}
html,body{width:932px;height:1200px;overflow:hidden}
body{background:var(--page-bg);font-family:"Source Sans 3",Arial,sans-serif;color:var(--ink);position:relative}
.page{position:absolute;left:12px;top:11px;width:908px;height:1177px;background:var(--white)}

/* hero */
.hero{position:absolute;left:0;top:0;width:908px;height:485px;overflow:hidden}
.hero-scene{position:absolute;inset:0;background:linear-gradient(180deg,var(--sky-top) 0%,var(--sky-low) 52%,var(--grass) 66%,var(--grass-deep) 100%)}
.logo-sign{position:absolute;left:26px;top:42px;width:215px;height:70px;border-radius:4px;background:linear-gradient(180deg,#f4f6f7,#c9ced2);box-shadow:0 2px 4px rgba(0,0,0,.2);display:flex;flex-direction:column;align-items:center;justify-content:center;line-height:1}
.logo-sign span{font-family:"Source Sans 3",Arial,sans-serif;font-weight:700;color:#444;letter-spacing:.5px}
.logo-sign .l1{font-size:27px}
.logo-sign .l2{font-size:15px;margin-top:4px}
.hanger{position:absolute;top:-12px;width:2px;height:64px;background:#222}
.main-nav{position:absolute;top:67px;left:396px;display:flex;gap:17px;font-family:"Patrick Hand",cursive;font-size:15px;text-transform:uppercase;color:#333}
.main-nav .active{color:var(--lime)}
.welcome{position:absolute;left:353px;top:199px;width:264px;height:216px;border-radius:4px 4px 0 0;background:linear-gradient(180deg,#8cbc2c 0%,#4d6a1b 50%,#0a0a0a 100%);padding:18px 13px 0;color:var(--white);font-size:10.6px;font-weight:600;line-height:14px}
.welcome p+p{margin-top:14px}

/* goal */
.goal{position:absolute;left:0;top:485px;width:908px;height:210px;background:#f3f6f7;text-align:center;box-shadow:inset 0 10px 10px -8px rgba(0,0,0,.25)}
.goal h1{margin-top:36px;font-size:21px;font-weight:600;color:var(--lime-text)}
.goal p{margin:12px auto 0;width:790px;font-size:13px;line-height:18px;color:#444}
.btn-solid{display:inline-block;margin-top:14px;width:186px;height:27px;line-height:27px;background:var(--lime);color:var(--white);font-size:13px;font-weight:600}

/* features */
.features{position:absolute;left:0;top:695px;width:908px;height:237px;display:flex}
.feature{flex:1;text-align:center;padding-top:30px}
.feature:nth-child(1){background:var(--col-a)}
.feature:nth-child(2){background:var(--col-b)}
.feature:nth-child(3){background:var(--col-c)}
.feature svg{width:56px;height:56px;display:block;margin:0 auto}
.feature h2{margin-top:11px;font-size:15px;font-weight:600;color:var(--lime-text)}
.feature p{margin:7px auto 0;width:215px;font-size:10.5px;line-height:14.5px;color:var(--muted)}
.btn-outline{display:inline-block;margin-top:12px;width:156px;height:20px;line-height:17px;border:1.5px solid #333;border-radius:10px;font-size:10.5px;font-weight:600;color:#333}

/* footer */
.site-footer{position:absolute;left:0;top:932px;width:908px;height:217px;background:var(--footer);color:var(--white);font-size:10.5px;font-weight:600;text-transform:uppercase}
.f-col{position:absolute;top:32px}
.f-col h3{font-size:10.5px;font-weight:600;color:var(--lime)}
.f-nav{left:60px}
.f-nav ul{list-style:none;margin-top:17px;line-height:15.2px}
.f-contact{left:218px}
.f-contact .row{display:flex;gap:6px;margin-top:17px;line-height:15.2px}
.f-contact .row+.row{margin-top:15px}
.f-contact svg{width:12px;height:12px;flex:none;margin-top:1px}
.f-hours{left:478px}
.f-hours p{margin-top:17px;line-height:15.2px;text-transform:none}
.f-brand{position:absolute;left:700px;top:78px;width:175px;text-align:center;font-weight:700;line-height:1}
.f-brand .l1{display:block;font-size:32px}
.f-brand .l2{display:block;font-size:20px;margin-top:6px}
.copy-bar{position:absolute;left:0;top:1149px;width:908px;height:28px;background:var(--lime);display:flex;align-items:center;justify-content:space-between;padding:0 21px}
.copy-bar small{font-size:8px;font-weight:700;color:var(--white)}
.social{display:flex;gap:4px}
.social span{width:15px;height:15px;border-radius:50%;border:1.5px solid var(--white)}
</style>
</head>
<body>
<div class="page">
  <header class="hero">
    <div class="hero-scene" role="img" aria-label="Cartoon illustration of a sunny park with clouds, colourful houses, a city skyline, trees, balloons and children waving"></div>
    <div class="logo-sign">
      <i class="hanger" style="left:58px;top:-54px"></i>
      <i class="hanger" style="left:166px;top:-54px"></i>
      <span class="l1">PLAYPATH</span>
      <span class="l2">URGENT CARE</span>
    </div>
    <nav class="main-nav">
      <span class="active">Home</span><span>About Us</span><span>Services</span><span>FAQs</span><span>Patient Forms</span><span>Insurance Info</span><span>Contact Us</span>
    </nav>
    <div class="welcome">
      <p>Welcome to PLAYPATH Urgent Care where we specialize in providing urgent care for kids. We are open late nights and weekends.</p>
      <p>Our services include xrays, breathing treatments, labs, laceration repair, removing all sorts of items from noses and ears, treating bug and animal bites, diagnosing and treating flu, strep, mono, RSV, and much more.</p>
      <p>The team at PLAYPATH Urgent Care is here for you! Contact us today!</p>
    </div>
  </header>

  <section class="goal">
    <h1>Our goal is to preserve the health of your child</h1>
    <p>We are committed to providing all of our young patients with the highest standard of care available. We specialize in treatment for acute conditions. Our physicians are dedicated to providing the most advanced and comprehensive care for children of all ages, including infants, children and adolescents.</p>
    <span class="btn-solid">MORE ON OUR SERVICES</span>
  </section>

  <section class="features">
    <div class="feature">
      <svg viewBox="0 0 56 56" fill="none" stroke="#acd037" stroke-width="1.5"><circle cx="28" cy="28" r="27"/><circle cx="19" cy="23" r="4"/><circle cx="37" cy="23" r="4"/><circle cx="28" cy="21" r="5"/><path d="M12 37c0-5 3-8 7-8M44 37c0-5-3-8-7-8M19 39c0-6 4-10 9-10s9 4 9 10z"/></svg>
      <h2>Our Staffs</h2>
      <p>Lorem ipsum dolor sit amet, consectetuer adipis elit, sed diam nonummy nibh euismod tincidunt laoreet dolore magna aliquam erat volutpat.</p>
      <span class="btn-outline">LEARN MORE</span>
    </div>
    <div class="feature">
      <svg viewBox="0 0 56 56" fill="none" stroke="#acd037" stroke-width="1.5"><circle cx="28" cy="28" r="27"/><path d="M11 16h20v14H19l-5 5v-5h-3z"/><path d="M25 26h20v14h-3v5l-5-5H25z"/><text x="16" y="27" font-size="10" fill="#acd037" stroke="none" font-family="Source Sans 3,sans-serif" font-weight="700">Q</text><text x="32" y="37" font-size="10" fill="#acd037" stroke="none" font-family="Source Sans 3,sans-serif" font-weight="700">A</text></svg>
      <h2>Frequently Asked Questions</h2>
      <p>Lorem ipsum dolor sit amet, consectetuer adipis elit, sed diam nonummy nibh euismod tincidunt laoreet dolore magna aliquam erat volutpat.</p>
      <span class="btn-outline">LEARN MORE</span>
    </div>
    <div class="feature">
      <svg viewBox="0 0 56 56" fill="none" stroke="#acd037" stroke-width="1.5"><circle cx="28" cy="28" r="27"/><path d="M17 12h17l6 6v26H17z"/><path d="M34 12v6h6M21 20h9M21 25h14M21 30h14M21 35h14M21 40h10"/></svg>
      <h2>Patient Forms</h2>
      <p>Lorem ipsum dolor sit amet, consectetuer adipis elit, sed diam nonummy nibh euismod tincidunt laoreet dolore magna aliquam erat volutpat.</p>
      <span class="btn-outline">LEARN MORE</span>
    </div>
  </section>

  <footer class="site-footer">
    <div class="f-col f-nav">
      <h3>Navigation</h3>
      <ul><li>Home</li><li>About Us</li><li>Services</li><li>FAQs</li><li>Patient Forms</li><li>Insurance Info</li><li>Contact Us</li></ul>
    </div>
    <div class="f-col f-contact">
      <h3>Contact Info</h3>
      <div class="row"><svg viewBox="0 0 12 12"><path d="M6 0.5a4 4 0 0 0-4 4c0 3 4 7 4 7s4-4 4-7a4 4 0 0 0-4-4z" fill="#fff"/><circle cx="6" cy="4.5" r="1.5" fill="#1b1b1b"/></svg><span>45 Maple Grove Drive<br>Suite 210<br>Building B<br>Riverton, NY 11800</span></div>
      <div class="row"><svg viewBox="0 0 12 12"><path d="M1 4c0-2 2-3 5-3s5 1 5 3v1H8.5V3.8h-5V5H1z" fill="#fff"/><rect x="2.5" y="5.5" width="7" height="5.5" rx="1" fill="#fff"/></svg><span>555-010-2468</span></div>
      <div class="row"><svg viewBox="0 0 12 12"><rect x="0.5" y="2" width="11" height="8" fill="#fff"/><path d="M0.5 2l5.5 5 5.5-5" stroke="#1b1b1b" fill="none"/></svg><span>info@playpathurgentcare.com</span></div>
    </div>
    <div class="f-col f-hours">
      <h3>Office Hours</h3>
      <p>Open Monday-Friday 4pm-10pm<br>Weekends 10am-6pm</p>
    </div>
    <div class="f-brand"><span class="l1">PLAYPATH</span><span class="l2">URGENT CARE</span></div>
  </footer>

  <div class="copy-bar">
    <small>COPYRIGHT © 2016 PLAYPATH URGENT CARE. ALL RIGHTS RESERVED.</small>
    <div class="social"><span></span><span></span><span></span></div>
  </div>
</div>
</body>
</html>
```